HPS business cards

(Generators . Lighting Towers . De-watering Pumps . Compressors) put under the logo please. my details are Owen Pritchard (Director) 0461527390 harbourpinesupply@postvale.net

```html
<!DOCTYPE html>
<html lang="en">
<head>
<meta charset="utf-8">
<title>HPS Business Cards</title>
<link href="https://fonts.googleapis.com/css2?family=Montserrat:wght@500;600;700&display=swap" rel="stylesheet">
<style>
  :root {
    --page-bg: #e6e7e9;
    --card-bg: #333333;
    --emboss: #8c8c8c;
    --emboss-soft: #808080;
    --gold: #e29e2e;
    --name-gold: #d8902f;
    --white: #ffffff;
  }
  * { margin: 0; padding: 0; box-sizing: border-box; }
  html, body {
    width: 1200px; height: 1200px; overflow: hidden;
    background: var(--page-bg);
    font-family: "Montserrat", sans-serif;
  }
  .card {
    position: absolute; left: 274px; width: 666px; height: 411px;
    background: var(--card-bg);
  }
  .card--front { top: 121px; }
  .card--back { top: 661px; }

  .front-brand {
    position: absolute; left: 0; right: 0; top: 88px;
    display: flex; flex-direction: column; align-items: center;
  }
  .brand-square {
    width: 60px; height: 60px; background: var(--emboss);
  }
  .front-brand .brand-name {
    margin-top: 22px;
    font-size: 40px; font-weight: 700; letter-spacing: 1px;
    color: var(--emboss); white-space: nowrap;
  }
  .tagline {
    position: absolute; left: 60px; right: 60px; top: 274px;
    text-align: center; font-size: 17.5px; font-weight: 600; line-height: 25px;
    color: var(--emboss-soft);
  }

  .back-brand {
    position: absolute; left: 330px; width: 286px; top: 58px;
    display: flex; flex-direction: column; align-items: center;
  }
  .back-brand .brand-square {
    width: 46px; height: 46px; background: var(--gold);
  }
  .back-brand .brand-name {
    margin-top: 14px;
    font-size: 22px; font-weight: 700; letter-spacing: 0.5px;
    color: var(--gold); white-space: nowrap;
  }
  .person {
    position: absolute; left: 60px; top: 232px;
  }
  .person-name {
    font-size: 24px; font-weight: 600; letter-spacing: 1px;
    color: var(--name-gold);
  }
  .person-role {
    margin-top: 2px; font-size: 19px; font-weight: 500; color: var(--white);
  }
  .contact-list { list-style: none; margin-top: 22px; }
  .contact-item {
    display: flex; align-items: center; gap: 10px;
    font-size: 17.5px; font-weight: 600; color: var(--white);
    height: 30px;
  }
  .contact-icon { width: 18px; height: 18px; flex: none; }
</style>
</head>
<body>
  <section class="card card--front">
    <div class="front-brand">
      <div class="brand-square"></div>
      <div class="brand-name">HARBOUR PINE SUPPLY</div>
    </div>
    <p class="tagline">Generators | Lighting Towers | De-watering Pumps |<br>Compressors</p>
  </section>

  <section class="card card--back">
    <div class="back-brand">
      <div class="brand-square"></div>
      <div class="brand-name">HARBOUR PINE SUPPLY</div>
    </div>
    <div class="person">
      <div class="person-name">OWEN PRITCHARD</div>
      <div class="person-role">Director</div>
      <ul class="contact-list">
        <li class="contact-item">
          <svg class="contact-icon" viewBox="0 0 18 18" aria-hidden="true">
            <rect x="4" y="1" width="10" height="16" rx="1.5" fill="none" stroke="#e29e2e" stroke-width="1.6"/>
            <line x1="7.5" y1="14" x2="10.5" y2="14" stroke="#e29e2e" stroke-width="1.4"/>
          </svg>
          0461527390
        </li>
        <li class="contact-item">
          <svg class="contact-icon" viewBox="0 0 18 18" aria-hidden="true">
            <rect x="1" y="4" width="16" height="11" fill="#e29e2e"/>
            <polyline points="1,4 9,10 17,4" fill="none" stroke="#333333" stroke-width="1.4"/>
          </svg>
          harbourpinesupply@postvale.net
        </li>
      </ul>
    </div>
  </section>
</body>
</html>
```